Company website for an international IT business

We require a website for our business, Corvell Solutions. The business has two primary areas: Horizons, which includes two machine learning/deep learning based products and IT consultancy, which is the service we provide to other businesses.

We bridge cutting-edge research to market.

STYLING:
The site can be on single page or multi-page. This is fully open to suggestion. So long as the look and feel are consistent. Currently, we have no strong preference for colors, styles or layouts.
You can find the logo of our website in the attachment “Corvell-logo.png” and “Corvell-logo-landscape.png”.

CONTENT:
You can find the text of the website in “Website-Content.pdf”, which explains the services and products of our business. The format of the text is also open to suggestion - including breaking up the text into visually appealing sections.
We would also like to include suitable images on the website so that it does not appear to be a text-heavy page. We are happy to have placeholder images on stock image sites if needed. We are open to suggestions on placing of images

ATTACHMENT:

Industry/Entity Type

It Company

Coding

Coded - Design and coding required

Number of Pages Required

1 page

Colors

Designer to choose colors to be used in the design.

Requirements
Must have
• A full description of the requirement is in the attachment "Website-Content.pdf"
• The design must have HTML/CSS, and all resources relevant (images, fonts etc)
• We are
Nice to have
• We are open to suggestions on top of the requirement, please reach out and communicate.

```html
<!DOCTYPE html>
<html lang="en">
<head>
<meta charset="utf-8">
<title>Corvell Solutions</title>
<link href="https://fonts.googleapis.com/css2?family=Roboto:wght@300;400;500;700&family=Open+Sans:wght@400;600&display=swap" rel="stylesheet">
<style>
:root{
  --blue:#1e88d9;
  --blue-dark:#14609e;
  --navy:#0f3f6e;
  --ink:#222831;
  --text:#6b7178;
  --light:#f3f5f7;
  --consult-bg:#eef5fb;
  --grey-arc:#b9bec4;
  --footer-bg:#ffffff;
  --line:#e2e5e8;
  --white:#ffffff;
}
*{box-sizing:border-box;margin:0;padding:0}
html,body{width:1200px;height:3240px;overflow:hidden}
body{font-family:"Open Sans",Arial,sans-serif;color:var(--text);background:var(--white);position:relative}
h1,h2,h3,h4{font-family:"Roboto",Arial,sans-serif;color:var(--ink)}

/* HERO */
.hero{position:absolute;top:0;left:0;width:1200px;height:580px;overflow:hidden}
.hero-photo{position:absolute;inset:0;background:linear-gradient(180deg,#5b6470 0%,#3b434d 45%,#2a2f36 75%,#464d55 100%)}
.hero-shade{position:absolute;inset:0;background:rgba(10,20,35,.35)}
.topnav{position:absolute;top:0;left:0;right:0;height:64px;display:flex;align-items:center;padding:0 100px}
.nav-brand{display:flex;align-items:center;gap:12px;font-family:"Roboto",sans-serif;font-weight:500;color:var(--white);font-size:18px}
.nav-brand .dot{width:48px;height:48px;border-radius:50%;background:var(--white)}
.nav-links{margin-left:auto;display:flex;gap:38px;list-style:none;font-family:"Roboto",sans-serif;font-size:15px;color:var(--white)}
.nav-links .active{color:var(--blue)}
.hero-mark{position:absolute;left:550px;top:180px;width:100px;height:100px;border-radius:50%;background:var(--white)}
.hero-title{position:absolute;top:318px;width:100%;text-align:center;color:var(--white);font-size:64px;font-weight:500;letter-spacing:1px}
.hero-sub{position:absolute;top:402px;width:100%;text-align:center;color:var(--white);font-size:20px}
.hero-dots{position:absolute;top:512px;width:100%;display:flex;justify-content:center;gap:8px}
.hero-dots span{width:10px;height:10px;border-radius:50%;border:1.5px solid var(--white)}
.hero-dots span:first-child{background:var(--white)}

/* SECTION TITLES */
.section-title{text-align:center;font-size:34px;font-weight:700;letter-spacing:.5px}
.section-lead{text-align:center;font-size:14px;line-height:1.6;width:520px;margin:14px auto 0}

/* WHAT IS */
.about{position:absolute;top:580px;left:0;width:1200px;height:500px;padding-top:98px}
.features{display:flex;justify-content:center;gap:70px;margin-top:60px}
.feature{width:260px;text-align:center}
.feature svg{height:70px}
.feature h3{font-size:19px;font-weight:700;margin:20px 0 10px}
.feature p{font-size:12.5px;line-height:1.6}

/* HOW WE HELP */
.help{position:absolute;top:1080px;left:0;width:1200px;height:420px;overflow:hidden}
.help-photo{position:absolute;inset:0;background:linear-gradient(90deg,#1c5f9c 0%,#2377c1 55%,#2e8ad0 100%)}
.help-shade{position:absolute;inset:0;background:rgba(20,90,160,.55)}
.help .section-title{position:relative;color:var(--white);font-weight:500;padding-top:92px}
.steps{position:relative;display:flex;justify-content:center;align-items:flex-start;gap:0;margin-top:48px}
.step{width:220px;text-align:center;color:var(--white);font-size:14px;line-height:1.5}
.step .ring{width:120px;height:120px;border-radius:50%;border:3px solid var(--white);margin:0 auto 22px;display:flex;align-items:center;justify-content:center}
.step-arrow{width:150px;height:120px;display:flex;align-items:center;justify-content:center}

/* HORIZONS */
.horizons{position:absolute;top:1500px;left:0;width:1200px;height:940px;padding-top:72px}
.horizons .section-lead{margin-top:10px}
.products{display:flex;justify-content:center;gap:56px;margin-top:50px}
.product{width:460px;text-align:center}
.product-photo{height:400px}
.product-photo.drive{background:linear-gradient(135deg,#b8463a 0%,#7d8a94 50%,#c9cdd1 100%)}
.product-photo.desk{background:linear-gradient(135deg,#d7d9dc 0%,#8e949b 55%,#4b5158 100%)}
.product h3{font-size:20px;font-weight:700;margin:44px 0 14px;letter-spacing:.5px}
.product p{font-size:12.5px;line-height:1.6;padding:0 30px}
.btn{display:inline-block;margin-top:34px;border:2px solid var(--blue);color:var(--blue);font-family:"Roboto",sans-serif;font-weight:500;font-size:13px;padding:9px 20px}

/* CONSULTANCY */
.consultancy{position:absolute;top:2440px;left:0;width:1200px;height:420px;background:var(--consult-bg)}
.consult-text{position:absolute;left:96px;top:60px;width:520px}
.consult-text h2{font-size:30px;font-weight:700;color:var(--navy)}
.consult-text p{font-size:12.5px;line-height:1.6;margin-top:18px}
.consult-text .btn{margin-top:26px}
.cycle{position:absolute;left:700px;top:20px}

/* FOOTER */
.footer{position:absolute;top:2860px;left:0;width:1200px;height:320px;background:var(--footer-bg);border-top:1px solid var(--line)}
.footer-brand{position:absolute;left:100px;top:60px;display:flex;align-items:center;gap:12px;font-family:"Roboto",sans-serif;font-weight:500;font-size:20px;color:var(--blue)}
.footer-brand .dot{width:64px;height:64px;border-radius:50%;background:var(--blue)}
.fcol{position:absolute;top:50px}
.fcol h4{font-size:17px;font-weight:700;margin-bottom:18px;letter-spacing:.3px}
.fcol ul{list-style:none;font-size:12px;line-height:2}
.fcol p{font-size:12px;line-height:1.6}
.col-links{left:410px}
.col-news{left:580px;width:240px}
.col-contact{left:900px;width:220px}
.email-field{margin-top:14px;border-bottom:1px solid var(--line);font-size:12px;padding:6px 0;color:#a0a5ab;width:150px}
.subscribe{margin-top:14px;display:inline-block;border:1.5px solid var(--blue);color:var(--blue);font-size:12px;padding:5px 14px;font-family:"Roboto",sans-serif}
.contact-row{display:flex;gap:10px;align-items:flex-start;margin-bottom:10px}
.socials{display:flex;gap:8px;position:absolute;left:1020px;top:270px}
.socials span{width:24px;height:24px;border-radius:50%;background:var(--blue)}
.copyright{position:absolute;top:3180px;left:0;width:1200px;height:60px;background:var(--light);border-top:1px solid var(--line);font-size:12px;padding:22px 100px}
</style>
</head>
<body>

<header class="hero">
  <div class="hero-photo" role="img" aria-label="City skyline photograph at dusk"></div>
  <div class="hero-shade"></div>
  <nav class="topnav">
    <div class="nav-brand"><span class="dot"></span>Corvell</div>
    <ul class="nav-links">
      <li class="active">Home</li><li>Horizons</li><li>Consultancy</li><li>About Us</li><li>Contact</li>
      <li><svg width="16" height="16" viewBox="0 0 16 16"><circle cx="6.5" cy="6.5" r="5" fill="none" stroke="#fff" stroke-width="2"/><line x1="10" y1="10" x2="15" y2="15" stroke="#fff" stroke-width="2"/></svg></li>
    </ul>
  </nav>
  <div class="hero-mark"></div>
  <h1 class="hero-title">CORVELL SOLUTIONS</h1>
  <p class="hero-sub">Corvell Solutions is an IT consultancy firm with a difference</p>
  <div class="hero-dots"><span></span><span></span><span></span></div>
</header>

<section class="about">
  <h2 class="section-title">WHAT IS CORVELL</h2>
  <p class="section-lead">Corvell Solutions is an IT consultancy firm with a difference. We can provide IT expertise for your business at any stage - from initial idea to live systems.</p>
  <div class="features">
    <div class="feature">
      <svg viewBox="0 0 90 70" width="90"><rect x="14" y="8" width="62" height="42" rx="3" fill="none" stroke="var(--blue)" stroke-width="5"/><rect x="4" y="54" width="82" height="8" rx="2" fill="var(--blue)"/><circle cx="45" cy="29" r="9" fill="none" stroke="var(--blue)" stroke-width="4"/><circle cx="45" cy="29" r="3" fill="var(--blue)"/></svg>
      <h3>Software development</h3>
      <p>We can provide IT expertise for your business at any stage - from initial idea to live systems.</p>
    </div>
    <div class="feature">
      <svg viewBox="0 0 70 70" width="70" fill="var(--blue)">
        <rect x="0" y="0" width="14" height="14"/><rect x="18" y="0" width="14" height="14"/><rect x="36" y="0" width="14" height="14"/><rect x="54" y="0" width="14" height="14"/>
        <rect x="0" y="18" width="14" height="14"/><rect x="18" y="18" width="14" height="14"/><rect x="36" y="18" width="14" height="14"/><rect x="54" y="18" width="14" height="14"/>
        <rect x="0" y="36" width="14" height="14"/><rect x="18" y="36" width="14" height="14"/><rect x="36" y="36" width="14" height="14"/><rect x="54" y="36" width="14" height="14"/>
        <rect x="0" y="54" width="14" height="14"/><rect x="18" y="54" width="14" height="14"/><rect x="36" y="54" width="14" height="14"/><rect x="54" y="54" width="14" height="14"/>
      </svg>
      <h3>IOT System Design</h3>
      <p>We can provide IT expertise for your business at any stage - from initial idea to live systems.</p>
    </div>
    <div class="feature">
      <svg viewBox="0 0 70 70" width="70"><circle cx="35" cy="35" r="30" fill="none" stroke="var(--blue)" stroke-width="5"/><circle cx="35" cy="35" r="12" fill="none" stroke="var(--blue)" stroke-width="6"/><g stroke="var(--blue)" stroke-width="6"><line x1="35" y1="13" x2="35" y2="21"/><line x1="35" y1="49" x2="35" y2="57"/><line x1="13" y1="35" x2="21" y2="35"/><line x1="49" y1="35" x2="57" y2="35"/></g></svg>
      <h3>Machine learning solutions</h3>
      <p>We can provide IT expertise for your business at any stage - from initial idea to live systems.</p>
    </div>
  </div>
</section>

<section class="help">
  <div class="help-photo" role="img" aria-label="Photograph of a truck on a highway, tinted blue"></div>
  <div class="help-shade"></div>
  <h2 class="section-title">HOW CAN WE HELP</h2>
  <div class="steps">
    <div class="step">
      <div class="ring"><svg width="54" height="54" viewBox="0 0 54 54"><path d="M4 26 L50 4 L38 50 L26 32 Z" fill="#fff"/><path d="M26 32 L50 4" stroke="#2377c1" stroke-width="2"/></svg></div>
      Acquire more development capacity and get results fast
    </div>
    <div class="step-arrow"><svg width="60" height="40" viewBox="0 0 60 40"><path d="M0 20 H48 M36 6 L52 20 L36 34" fill="none" stroke="#fff" stroke-width="4"/></svg></div>
    <div class="step">
      <div class="ring"><svg width="60" height="50" viewBox="0 0 60 50" fill="#fff"><circle cx="30" cy="12" r="9"/><path d="M16 46 a14 14 0 0 1 28 0 Z"/><circle cx="11" cy="18" r="6"/><path d="M0 44 a11 11 0 0 1 18 -8 v8 Z"/><circle cx="49" cy="18" r="6"/><path d="M60 44 a11 11 0 0 0 -18 -8 v8 Z"/></svg></div>
      Avoid the overhead incurred by frequent scaling of your development team
    </div>
    <div class="step-arrow"><svg width="60" height="40" viewBox="0 0 60 40"><path d="M0 20 H48 M36 6 L52 20 L36 34" fill="none" stroke="#fff" stroke-width="4"/></svg></div>
    <div class="step">
      <div class="ring"><svg width="56" height="50" viewBox="0 0 56 50"><path d="M2 2 V48 H54" fill="none" stroke="#fff" stroke-width="3"/><path d="M8 40 L22 24 L32 32 L50 10" fill="none" stroke="#fff" stroke-width="4"/><path d="M40 8 H52 V20" fill="none" stroke="#fff" stroke-width="4"/></svg></div>
      Reach a wider spectrum of expertise
    </div>
  </div>
</section>

<section class="horizons">
  <h2 class="section-title">CORVELL HORIZONS</h2>
  <p class="section-lead">Corvell Horizons has developed two cutting edge products using machine learning and deep learning</p>
  <div class="products">
    <article class="product">
      <div class="product-photo drive" role="img" aria-label="Photograph of a driver at the wheel of a truck"></div>
      <h3>WAYLINE</h3>
      <p>The primary cause of accidents on the road are caused by human error. Of these driver distraction and fatigue are the real problem. Wayline is a system that monitors drivers to make every journey safer – safer for the driver and safer for other road users.</p>
      <span class="btn">READ MORE</span>
    </article>
    <article class="product">
      <div class="product-photo desk" role="img" aria-label="Photograph of hands using a calculator beside financial charts"></div>
      <h3>LEDGERLANE</h3>
      <p>Ledgerlane is a machine learning system that tracks and analyses live used car trading markets. It learns every aspect of a car sale, through which, it creates powerful market intelligence for all parties in the used car ecosystem.</p>
      <span class="btn">READ MORE</span>
    </article>
  </div>
</section>

<section class="consultancy">
  <div class="consult-text">
    <h2>IT CONSULTANCY</h2>
    <p>The consultancy section is summarised in the "Corvell-Consultancy.pdf". The text in the deck has the spirit of the information we wish to convey. The presentation is open to suggestion and interpretation.</p>
    <p>It should also include a portfolio section, which can be filled with placeholder images and text in the design.</p>
    <span class="btn">READ MORE</span>
  </div>
  <svg class="cycle" width="380" height="380" viewBox="0 0 380 380">
    <g font-family="Roboto, sans-serif" font-size="14" font-weight="500" fill="#fff">
      <path d="M190 30 A160 160 0 0 1 342 230 L270 210 A85 85 0 0 0 190 105 Z" fill="var(--blue)"/>
      <path d="M335 248 A160 160 0 0 1 60 290 L120 245 A85 85 0 0 0 265 225 Z" fill="var(--grey-arc)"/>
      <path d="M50 275 A160 160 0 0 1 172 31 L180 106 A85 85 0 0 0 112 232 Z" fill="#9aa0a7"/>
      <path d="M325 230 L352 234 L330 250 Z" fill="var(--blue)"/>
      <text x="262" y="108" transform="rotate(50 262 108)">DEFINE</text>
      <text x="190" y="330" transform="rotate(-10 190 330)">BUILD</text>
      <text x="78" y="210" transform="rotate(-75 78 210)">DELIVER</text>
    </g>
  </svg>
</section>

<footer class="footer">
  <div class="footer-brand"><span class="dot"></span>Corvell</div>
  <div class="fcol col-links">
    <h4>QUICK LINKS</h4>
    <ul><li>Help</li><li>FAQ</li><li>Support</li><li>Sitemap</li><li>Terms of Use</li><li>Privacy Statement</li></ul>
  </div>
  <div class="fcol col-news">
    <h4>NEWSLETTER SUBSCRIPTION</h4>
    <p>Register your email below to get information about us</p>
    <div class="email-field">Email address</div>
    <span class="subscribe">SUBSCRIBE</span>
  </div>
  <div class="fcol col-contact">
    <h4>CONTACT US</h4>
    <div class="contact-row"><svg width="12" height="16" viewBox="0 0 12 16"><path d="M6 0 A6 6 0 0 1 12 6 C12 10 6 16 6 16 C6 16 0 10 0 6 A6 6 0 0 1 6 0 Z" fill="var(--blue)"/><circle cx="6" cy="6" r="2" fill="#fff"/></svg><p>412 Harbour Row, Suite 18,<br>Westbrook, OR 97410</p></div>
    <div class="contact-row"><svg width="14" height="14" viewBox="0 0 14 14"><path d="M2 1 L5 1 L6 4 L4 5.5 A8 8 0 0 0 8.5 10 L10 8 L13 9 L13 12 A1 1 0 0 1 12 13 A11 11 0 0 1 1 2 A1 1 0 0 1 2 1 Z" fill="var(--blue)"/></svg><p>+1 (503) 555-0192</p></div>
    <div class="contact-row"><svg width="14" height="12" viewBox="0 0 14 12"><rect x="0.5" y="0.5" width="13" height="11" fill="none" stroke="var(--blue)"/><path d="M0.5 0.5 L7 6 L13.5 0.5" fill="none" stroke="var(--blue)"/></svg><p>hello@corvellsolutions.example</p></div>
  </div>
  <div class="socials"><span></span><span></span><span></span></div>
</footer>
<div class="copyright">Copyright © 2019, Corvell Solutions . All rights reserved.</div>

</body>
</html>
```